Pelverhook LLC
Business Cards & Stationary
Professional
Tobias Wendell
President
482 Orchard Crest Road
Dunmore Falls, NJ 07934-2718
tobias.wendell@mailvexo.com
www.pelverhook.com
I require the full suite of stationary products i.e.:- Business card, letterhead, envelope, fax cover sheet, thank you cards, invoice etc.
Just the logo on the back of the card.

```html
<!DOCTYPE html>
<html lang="en">
<head>
<meta charset="utf-8">
<title>Pelverhook LLC – Business Cards</title>
<link href="https://fonts.googleapis.com/css2?family=Arimo:wght@400;700&display=swap" rel="stylesheet">
<style>
  :root {
    --backdrop: #e9e6e1;
    --card-white: #ffffff;
    --card-grey: #e4e6ea;
    --navy: #1b2f86;
    --navy-deep: #14206a;
    --sky: #3fb7e8;
    --brand-blue: #1a5aa8;
    --text-dark: #333840;
    --text-mid: #555b63;
    --rule-blue: #3c7fd0;
  }
  * { box-sizing: border-box; margin: 0; padding: 0; }
  html, body { width: 1200px; height: 703px; overflow: hidden; }
  body {
    background: var(--backdrop);
    font-family: "Arimo", Arial, sans-serif;
    position: relative;
  }
  .card {
    position: absolute;
    width: 466px;
    height: 264px;
    border-radius: 14px;
    overflow: hidden;
    box-shadow: 0 6px 14px rgba(0,0,0,0.22);
  }
  .brand-dot { flex: none; border-radius: 50%; background: var(--brand-blue); }
  .brand-name { font-weight: 700; color: var(--brand-blue); letter-spacing: 1px; white-space: nowrap; }

  /* Front card */
  .card-front {
    left: 115px; top: 110px;
    background: linear-gradient(180deg, var(--card-white) 0%, var(--card-grey) 100%);
  }
  .front-brand {
    position: absolute; left: 22px; top: 112px;
    display: flex; align-items: center; gap: 8px;
  }
  .front-brand .brand-dot { width: 20px; height: 20px; }
  .front-brand .brand-name { font-size: 19px; }
  .front-rule {
    position: absolute; left: 256px; top: 58px;
    width: 2px; height: 122px; background: var(--rule-blue);
  }
  .contact {
    position: absolute; left: 268px; top: 52px;
    color: var(--text-dark); white-space: nowrap;
  }
  .contact-name { font-size: 16px; font-weight: 700; color: var(--brand-blue); }
  .contact-title { font-size: 10.5px; margin-top: 2px; }
  .contact-lines { margin-top: 12px; font-size: 10px; line-height: 14px; color: var(--text-mid); }
  .contact-lines .label { display: inline-block; width: 32px; }
  .front-band {
    position: absolute; left: 0; right: 0; bottom: 0; height: 22px;
    background: linear-gradient(90deg, var(--sky) 0%, var(--navy) 60%, var(--navy-deep) 100%);
    text-align: center;
  }
  .front-band .url {
    color: #fff; font-size: 12px; letter-spacing: 1px; line-height: 22px;
  }

  /* Back cards */
  .back-brand { position: absolute; display: flex; align-items: center; gap: 12px; }
  .back-brand .brand-dot { width: 28px; height: 28px; }
  .back-brand .brand-name { font-size: 28px; }
  .back-url { position: absolute; right: 32px; font-size: 12px; letter-spacing: 1px; }

  .card-back-blue {
    left: 648px; top: 60px;
    background: linear-gradient(90deg, var(--sky) 0%, #2a6fc4 40%, var(--navy) 75%, var(--navy-deep) 100%);
  }
  .card-back-blue .back-brand { left: 64px; top: 112px; }
  .card-back-blue .brand-dot { background: #fff; }
  .card-back-blue .brand-name { color: #fff; }
  .card-back-blue .back-url { top: 220px; color: #fff; }

  .card-back-white {
    left: 403px; top: 405px;
    background: linear-gradient(180deg, var(--card-white) 0%, var(--card-grey) 100%);
  }
  .card-back-white .back-brand { left: 64px; top: 100px; }
  .card-back-white .back-url { top: 216px; color: var(--brand-blue); }
</style>
</head>
<body>

  <section class="card card-front">
    <div class="front-brand">
      <span class="brand-dot"></span>
      <span class="brand-name">PELVERHOOK LLC</span>
    </div>
    <div class="front-rule"></div>
    <div class="contact">
      <div class="contact-name">Tobias Wendell</div>
      <div class="contact-title">President</div>
      <div class="contact-lines">
        482 Orchard Crest Road<br>
        Dunmore Falls, NJ 07934-2718<br>
        Phone: 201.555.0143<br>
        <span class="label">Cell</span>201.555.0178<br>
        <span class="label">Fax</span>201.555.0143<br>
        Email: tobias.wendell@mailvexo.com
      </div>
    </div>
    <div class="front-band"><span class="url">www.pelverhook.com</span></div>
  </section>

  <section class="card card-back-blue">
    <div class="back-brand">
      <span class="brand-dot"></span>
      <span class="brand-name">PELVERHOOK</span>
    </div>
    <span class="back-url">www.pelverhook.com</span>
  </section>

  <section class="card card-back-white">
    <div class="back-brand">
      <span class="brand-dot"></span>
      <span class="brand-name">PELVERHOOK</span>
    </div>
    <span class="back-url">www.pelverhook.com</span>
  </section>

</body>
</html>
```